Help our Velvet Parlour find our winning design! We're looking for a business card....

We’re a Velvet Parlour in NY specializing in custom-made cakes and unique desserts.
Our cakes combine flavor and art, each designed to match customer’s special event and theme.
We’d like a unique business card with a clean design that will combine French chic and artistic look & feel.
We’d like to differentiate ourselves from standard bakeries, please don’t offer cupcake images :-)
Our logo is peach-pink and brown and we’d love to use these colors ( . Another color that can be added is gold - or feel free to suggest!

Target Market(s)

Women, ages 25-55

Industry/Entity Type

Boutique

Contact Information for Business Card

Text on card:
Logo
Velvet Parlour by Nadia Fenwick

www.xxxxxxxx.com
xxx@xxxxx.com
(555) xxx-xxxx
F – xxxxxxxxxx
IG - xxxxxxxxx

Font styles to use
Sans Serif
Script

Requirements
Must have
• Logo
• Clean look
• French chic and artistic look & feel.
Nice to have
• Damask pattern
Should not have
• Cupcake images

```html
<!DOCTYPE html>
<html lang="en">
<head>
<meta charset="utf-8">
<title>Velvet Parlour – Business Card</title>
<link rel="stylesheet" href="https://fonts.googleapis.com/css2?family=Open+Sans:ital,wght@0,400;1,400&display=swap">
<style>
  :root {
    --backdrop: #5c5c5c;
    --card: #f7f7f7;
    --peach: #e9a08c;
    --peach-soft: #f3c9bc;
    --brown: #3b2b25;
    --ink: #4a4a4a;
    --rule: #8a8a8a;
  }
  * { box-sizing: border-box; margin: 0; padding: 0; }
  html, body {
    width: 1200px; height: 750px; overflow: hidden;
    background: var(--backdrop);
    font-family: "Open Sans", sans-serif;
  }
  .stage { position: relative; width: 1200px; height: 750px; }
  .card {
    position: absolute; top: 218px;
    width: 492px; height: 281px;
    background: var(--card);
    border-radius: 18px;
  }
  .card--front { left: 91px; }
  .card--back { left: 620px; }

  .brand-name {
    position: absolute;
    display: flex; align-items: center; justify-content: center; gap: 10px;
    font-family: "Open Sans", sans-serif;
    font-weight: 400;
    color: var(--brown);
    white-space: nowrap;
  }
  .brand-dot {
    flex: none; border-radius: 50%; background: var(--peach);
  }
  .card--front .brand-name {
    left: 27px; width: 220px; top: 73px; height: 36px; font-size: 26px;
  }
  .card--front .brand-dot { width: 9px; height: 9px; }
  .card--back .brand-name {
    left: 92px; width: 300px; top: 129px; height: 46px; font-size: 34px;
  }
  .card--back .brand-dot { width: 11px; height: 11px; }

  .contact-list {
    position: absolute; left: 45px; top: 156px;
    list-style: none;
  }
  .contact-list li {
    display: flex; align-items: center;
    height: 18.75px;
    font-size: 12.5px; color: var(--ink);
  }
  .contact-icon {
    width: 11px; height: 11px; margin-right: 6px; flex: none;
  }
  .contact-square {
    width: 10px; height: 10px; margin-right: 7px; flex: none;
    background: var(--peach); border-radius: 1px;
  }

  .cake-art {
    position: absolute; left: 303px; top: 74px;
    width: 153px; height: 181px;
    background: linear-gradient(180deg, var(--peach-soft), var(--peach));
    opacity: 0.75;
    border-radius: 6px 6px 2px 2px;
  }

  .tagline {
    position: absolute; left: 104px; top: 239px; width: 284px;
    display: flex; align-items: center; gap: 6px;
    font-size: 12.5px; font-style: italic; letter-spacing: 1px;
    color: var(--ink); white-space: nowrap;
  }
  .tagline::before, .tagline::after {
    content: ""; flex: 1; height: 1px; background: var(--rule);
  }
</style>
</head>
<body>
<main class="stage">
  <section class="card card--front">
    <div class="brand-name"><span class="brand-dot" aria-hidden="true"></span>Velvet Parlour</div>

    <ul class="contact-list">
      <li>
        <svg class="contact-icon" viewBox="0 0 12 12" aria-hidden="true">
          <path d="M1 4 Q6 0 11 4 L9.5 5.5 L8 4.5 L4 4.5 L2.5 5.5 Z M3 6 H9 L10 11 H2 Z" fill="var(--peach)"/>
        </svg>
        555.014.2290
      </li>
      <li>
        <svg class="contact-icon" viewBox="0 0 12 12" aria-hidden="true">
          <rect x="0.5" y="2.5" width="11" height="7.5" fill="var(--peach)"/>
          <path d="M0.5 2.5 L6 7 L11.5 2.5" fill="none" stroke="var(--card)" stroke-width="1"/>
        </svg>
        nadia@VelvetParlourNY.com
      </li>
      <li>
        <svg class="contact-icon" viewBox="0 0 12 12" aria-hidden="true">
          <g fill="none" stroke="var(--peach)" stroke-width="1">
            <circle cx="6" cy="6" r="5"/>
            <ellipse cx="6" cy="6" rx="2.2" ry="5"/>
            <path d="M1 6 H11 M2 3.5 H10 M2 8.5 H10"/>
          </g>
        </svg>
        www.VelvetParlourNY.com
      </li>
      <li><span class="contact-square" aria-hidden="true"></span>VelvetParlourNYCakes</li>
      <li><span class="contact-square" aria-hidden="true"></span>velvetparlournycakes</li>
    </ul>

    <div class="cake-art" role="img" aria-label="Line drawing of a four-tier cake topped with a heart, in peach-pink"></div>
  </section>

  <section class="card card--back">
    <div class="brand-name"><span class="brand-dot" aria-hidden="true"></span>Velvet Parlour</div>
    <p class="tagline">Boutique Bakery by Nadia Fenwick</p>
  </section>
</main>
</body>
</html>
```